QTR Business Card

Harborline Capital Partners is a successful and reputable financial services company.Our main services are home loans, commercial loans, vehicle finance and equipment finance. We also do development finance for property developers. Our company is always evolving to always be an industry leader in best financial service practices with access to the largest range of lenders in the country.

We want the business card to reflect our national finance company. Modern, professional corporate image. At the same time the concept of Harborline Capital Partners is that we help build wealth for you but the process for the client is an enjoyable peaceful experience. Not stressful at all .....

Colors to be same as the logo .... gold silver black white as the options

On the reverse side of the card I wanted either just the logo symbol or the logo symbol and text of the logo ....

It could be on a black background ..... or silver or gold .... want it to be quite striking to look at when you first see the card.

On the other side of the card I wanted the following details:

Doran Pelham
Director

0498 372 604

doran@hbcpx.com.au

Po Box 852
Tarrow ACT 2694

www.hbcpx.com.au

ACN 918 264 057 (This can be in very small print and can be in the bottom corner of the card or somewhere not very prominent)
Updates

As requested Ive uploaded the logo file in both .ai and .pdf formats. Please let me know if you need anything else. Thanks

Reason: Still deciding on which design I like best. I will provide individual feedback as well.

```html
<!DOCTYPE html>
<html lang="en">
<head>
<meta charset="utf-8">
<title>QTR Business Card</title>
<link rel="stylesheet" href="https://fonts.googleapis.com/css2?family=Arvo:wght@400;700&display=swap">
<style>
  :root {
    --gold: #c99a2e;
    --gold-light: #e6c467;
    --ink: #111111;
    --card-black: #050505;
    --card-white: #fbfbfb;
    --backdrop: #e7e4df;
  }
  * { box-sizing: border-box; margin: 0; padding: 0; }
  html, body { width: 1200px; height: 900px; overflow: hidden; }
  body {
    background: var(--backdrop);
    font-family: "Arvo", Georgia, serif;
    color: var(--ink);
    position: relative;
  }
  .card {
    position: absolute;
    left: 290px;
    width: 620px;
    height: 354px;
    border-radius: 4px;
    box-shadow: 0 10px 28px rgba(0,0,0,.22);
    overflow: hidden;
  }
  .card--back {
    top: 80px;
    background: var(--card-black);
    display: flex;
    align-items: center;
    justify-content: center;
  }
  .brand-ring {
    width: 150px; height: 150px;
    border-radius: 50%;
    border: 7px solid var(--gold);
    display: flex; align-items: center; justify-content: center;
    color: var(--gold);
    font-weight: 400;
    font-size: 34px;
    letter-spacing: 4px;
  }
  .card--front { top: 466px; background: var(--card-white); }

  .brand {
    position: absolute;
    top: 38px; left: 0; right: 0;
    display: flex; align-items: center; justify-content: center; gap: 14px;
  }
  .brand__dot {
    width: 50px; height: 50px; border-radius: 50%;
    border: 4px solid var(--gold);
  }
  .brand__name {
    color: var(--gold);
    font-weight: 400;
    font-size: 20px;
    letter-spacing: 1.5px;
  }
  .holder {
    position: absolute; top: 118px; left: 0; right: 0;
    text-align: center;
  }
  .holder__name {
    color: var(--gold);
    font-weight: 700;
    font-size: 21px;
    letter-spacing: .5px;
    text-transform: uppercase;
  }
  .holder__role { font-weight: 700; font-size: 15px; margin-top: 2px; }

  .address {
    position: absolute; top: 150px; right: 30px;
    display: flex; align-items: flex-start; gap: 8px;
    text-align: right; font-weight: 700; font-size: 13px; line-height: 1.5;
  }
  .rule {
    position: absolute; left: 26px; right: 26px;
    height: 2px; background: var(--gold);
  }
  .rule--top { top: 200px; }
  .rule--bottom { top: 318px; }

  .contacts {
    position: absolute; top: 218px; left: 30px;
    list-style: none;
    font-weight: 700; font-size: 15px; line-height: 30px;
  }
  .contacts li { display: flex; align-items: center; gap: 12px; }
  .icon { width: 18px; height: 18px; flex: none; }
</style>
</head>
<body>

<section class="card card--back" aria-label="Card reverse">
  <div class="brand-ring">QTR</div>
</section>

<section class="card card--front" aria-label="Card front">
  <div class="brand">
    <span class="brand__dot"></span>
    <span class="brand__name">Harborline Capital Partners</span>
  </div>

  <div class="holder">
    <p class="holder__name">Doran Pelham</p>
    <p class="holder__role">Director</p>
  </div>

  <div class="address">
    <p>Po Box 852<br>Tarrow ACT 2694</p>
    <svg class="icon" viewBox="0 0 20 20" aria-hidden="true">
      <path d="M10 1a6 6 0 0 0-6 6c0 4.5 6 11 6 11s6-6.5 6-11a6 6 0 0 0-6-6zm0 8.3A2.3 2.3 0 1 1 10 4.7a2.3 2.3 0 0 1 0 4.6z" fill="var(--gold)"/>
    </svg>
  </div>

  <div class="rule rule--top"></div>

  <ul class="contacts">
    <li>
      <svg class="icon" viewBox="0 0 20 20" aria-hidden="true">
        <path d="M5 2l3 4-2 2c1 2.5 3.5 5 6 6l2-2 4 3-2 3C9 18 2 11 2 4z" fill="var(--gold)"/>
      </svg>
      0498 372 604
    </li>
    <li>
      <svg class="icon" viewBox="0 0 20 20" aria-hidden="true">
        <rect x="1" y="4" width="18" height="12" rx="1" fill="var(--gold)"/>
        <path d="M1.5 4.5L10 11l8.5-6.5" stroke="#fff" stroke-width="1.3" fill="none"/>
      </svg>
      doran@hbcpx.com.au
    </li>
    <li>
      <svg class="icon" viewBox="0 0 20 20" aria-hidden="true">
        <g fill="none" stroke="var(--gold)" stroke-width="1.4">
          <circle cx="10" cy="10" r="8"/>
          <ellipse cx="10" cy="10" rx="3.5" ry="8"/>
          <path d="M2 10h16M3.5 5.5h13M3.5 14.5h13"/>
        </g>
      </svg>
      www.hbcpx.com.au
    </li>
  </ul>

  <div class="rule rule--bottom"></div>
</section>

</body>
</html>
```